Project Report for American Indian and Alaska Native org (U.S.)

We need a report formatted/ design / layout.
We are a nonprofit organization that works on indigenous elder issues.
The report should reflect our logo color scheme.
Body font should be at least 11 point sans serif.
Ideally, headings and title would use fonts that are reminiscent of tribal cultures though not hard to read or whimsical/ unprofessional looking.

We have used some light script style fonts in the past -- nothing too cursive looking though.

The audience is public health professionals and tribal staff and leadership.

We want our organization's logo (QV7) and the project logo (brain health) incorporated into the title page.

We prefer the files to come back to us in an editable fashion + a pdf file.

Industry/Entity Type

tribal communities and public health officials

Font styles to use
Serif
Sans Serif

Requirements
Must have
• our logo and color scheme
Should not have
• headdress images

```html
<!DOCTYPE html>
<html lang="en">
<head>
<meta charset="utf-8">
<title>Tribal Law and Policy: Alzheimer's Disease and Related Dementia Issues</title>
<link rel="stylesheet" href="https://fonts.googleapis.com/css2?family=Bungee&family=Montserrat:wght@600;700;800&display=swap">
<style>
  :root {
    --clay: #b0564f;
    --teal: #4aa7aa;
    --ink: #4a4a4a;
    --paper: #ffffff;
  }
  * { margin: 0; padding: 0; box-sizing: border-box; }
  html, body { width: 848px; height: 1200px; overflow: hidden; background: var(--paper); }
  .cover {
    position: relative;
    width: 848px;
    height: 1200px;
    background: var(--paper);
    font-family: "Montserrat", Arial, sans-serif;
  }
  .project-mark {
    position: absolute;
    left: 41px;
    top: 41px;
    display: flex;
    align-items: center;
    gap: 12px;
  }
  .project-mark__dot {
    width: 66px;
    height: 66px;
    border-radius: 50%;
    background: var(--teal);
  }
  .project-mark__name {
    color: var(--teal);
    font-weight: 700;
    font-size: 17px;
    line-height: 1.2;
    text-transform: uppercase;
  }
  .rule {
    position: absolute;
    left: 0;
    width: 848px;
    height: 3px;
    background: var(--teal);
  }
  .rule--top { top: 315px; }
  .rule--bottom { top: 682px; }
  .title {
    position: absolute;
    left: 41px;
    top: 338px;
    color: var(--clay);
  }
  .title__main {
    font-family: "Bungee", "Impact", sans-serif;
    font-weight: 400;
    font-size: 78px;
    line-height: 106px;
    letter-spacing: 2px;
    text-transform: uppercase;
  }
  .title__sub {
    margin-top: 18px;
    font-weight: 800;
    font-size: 37px;
    line-height: 54px;
    text-transform: uppercase;
  }
  .credit {
    position: absolute;
    left: 41px;
    top: 1014px;
    color: var(--ink);
    font-weight: 700;
    font-size: 13.5px;
    line-height: 18px;
  }
  .client-mark {
    position: absolute;
    left: 41px;
    top: 1086px;
    display: flex;
    align-items: center;
    gap: 16px;
    color: var(--teal);
    font-weight: 700;
  }
  .client-mark__code { font-size: 52px; line-height: 1; }
  .client-mark__name { font-size: 21px; line-height: 1.15; text-transform: uppercase; }
</style>
</head>
<body>
  <main class="cover">
    <header class="project-mark">
      <span class="project-mark__dot"></span>
      <p class="project-mark__name">Tribal Elders Center<br>for Memory Wellness</p>
    </header>

    <div class="rule rule--top"></div>

    <h1 class="title">
      <span class="title__main">Tribal Law<br>and Policy:</span>
      <span class="title__sub" style="display:block">Alzheimer’s Disease and<br>Related Dementia Issues</span>
    </h1>

    <div class="rule rule--bottom"></div>

    <p class="credit">Prepared by RIDGELINE CONSULTING<br>october 27, 2021for:</p>

    <footer class="client-mark">
      <span class="client-mark__code">QV7</span>
      <span class="client-mark__name">Council for Native<br>Elder Vitality</span>
    </footer>
  </main>
</body>
</html>
```